Car Care labels for Soap,Interior Detailer,Wax,tire shine and All purpose cleaner

Project Overview:
We are launching a premium line of car care products under the GlenV brand and are looking for a high end, luxurious design for our product labels. The line includes a soap, a wax, an all-purpose cleaner, and an interior detailer. We already have a logo and color palette, and we have some basic bottle shapes picked out. Now we need a refined, eye catching label design that will elevate the look to something that feels upscale and classy, without being overly flashy.

Design Goals:
• Luxurious and Sophisticated: The overall aesthetic should feel premium and elegant. Think clean lines, refined typography, and a color scheme that reflects luxury like deep blacks, rich metallics, or subtle gradients that feel high end.
• Cohesive Branding: Each product label should feel like part of the same family, with a consistent design language across all items.
• Subtle and Tasteful: The design should be elegant but not overly busy. We want it to be eye catching on the shelf but still minimalist and refined.

```html
<!DOCTYPE html>
<html lang="en">
<head>
<meta charset="utf-8">
<title>GlenV Car Care Labels</title>
<link rel="stylesheet" href="https://fonts.googleapis.com/css2?family=Exo+2:ital,wght@0,800;1,800;1,900&display=swap">
<style>
  :root {
    --page: #ffffff;
    --label-black: #0b0b0c;
    --label-charcoal: #222326;
    --silver-light: #f4f4f4;
    --silver-mid: #a9abae;
    --silver-dark: #5d5f63;
    --ink-white: #ffffff;
    --wax-red: #e3101b;
    --wash-gold: #f2c511;
    --interior-cyan: #2fc7d9;
  }
  * { box-sizing: border-box; margin: 0; padding: 0; }
  html, body {
    width: 1200px; height: 1200px; overflow: hidden;
    background: var(--page);
  }
  .collection { position: relative; width: 1200px; height: 1200px; }

  .label {
    position: absolute;
    width: 292px; height: 476px;
    overflow: hidden;
    background:
      radial-gradient(ellipse 80% 40% at 50% 0%, var(--glow) 0%, transparent 70%),
      linear-gradient(180deg, var(--label-black) 0%, var(--label-charcoal) 45%, var(--label-black) 100%);
    font-family: "Exo 2", sans-serif;
  }
  .label--wax { left: 122px; top: 490px; --accent: var(--wax-red); --glow: rgba(227,16,27,0.35); }
  .label--wash { left: 486px; top: 562px; --accent: var(--wash-gold); --glow: rgba(242,197,17,0.3); }
  .label--interior { left: 825px; top: 472px; --accent: var(--interior-cyan); --glow: rgba(47,199,217,0.35); }

  .label__sweep {
    position: absolute; left: -40px; bottom: 60px;
    width: 420px; height: 170px;
    background: linear-gradient(100deg, transparent 0%, var(--accent) 45%, transparent 80%);
    opacity: 0.28;
    transform: rotate(-24deg);
    z-index: 0;
  }

  .brand {
    position: absolute; top: 46px; left: 0; width: 100%;
    display: flex; justify-content: center; align-items: center; gap: 8px;
    z-index: 2;
  }
  .brand__dot { width: 10px; height: 10px; border-radius: 50%; background: var(--accent); }
  .brand__name {
    font-weight: 800; font-style: normal; font-size: 30px;
    color: var(--ink-white); letter-spacing: 1px;
  }

  .title {
    position: absolute; left: 0; width: 100%;
    text-align: center;
    font-weight: 900; font-style: italic;
    text-transform: uppercase; line-height: 0.92;
    background: linear-gradient(180deg, var(--silver-light) 0%, var(--silver-mid) 48%, var(--silver-dark) 52%, var(--silver-light) 100%);
    -webkit-background-clip: text; background-clip: text;
    color: transparent;
    z-index: 2;
  }
  .label--wax .title { top: 120px; font-size: 72px; }
  .label--wash .title { top: 148px; font-size: 50px; }
  .label--interior .title { top: 138px; font-size: 52px; }

  .benefits {
    position: absolute; left: 0; width: 100%;
    list-style: none; text-align: center;
    font-weight: 800; font-style: italic; font-size: 19px;
    color: var(--ink-white); text-transform: uppercase; line-height: 1.1;
    z-index: 2;
  }
  .benefits li::before { content: "• "; color: var(--accent); }
  .label--wax .benefits { top: 280px; }
  .label--wash .benefits { top: 276px; }
  .label--interior .benefits { top: 266px; }

  .label__car {
    position: absolute; right: -10px; bottom: 14px;
    width: 250px; height: 128px;
    border-radius: 60px 30px 10px 40px;
    background: radial-gradient(ellipse at 45% 55%, var(--accent) 0%, rgba(0,0,0,0.6) 80%);
    opacity: 0.9;
    z-index: 1;
  }
  .label--interior .label__car { height: 136px; }

  .volume {
    position: absolute; left: 8px; bottom: 12px;
    font-weight: 800; font-style: italic; font-size: 13px;
    color: var(--silver-mid);
    z-index: 2;
  }
</style>
</head>
<body>
  <main class="collection">
    <section class="label label--wax">
      <div class="label__sweep"></div>
      <div class="brand"><span class="brand__dot"></span><span class="brand__name">GlenV</span></div>
      <h2 class="title">Spray<br>Wax</h2>
      <ul class="benefits"><li>High Gloss Wax</li><li>Easy &amp; Fast</li></ul>
      <div class="label__car" role="img" aria-label="Photo of a glossy red sports car, front three-quarter view"></div>
      <span class="volume">500ml</span>
    </section>

    <section class="label label--wash">
      <div class="label__sweep"></div>
      <div class="brand"><span class="brand__dot"></span><span class="brand__name">GlenV</span></div>
      <h2 class="title">Premium<br>Car Wash</h2>
      <ul class="benefits"><li>Wash &amp; Clean</li><li>Easy &amp; Fast</li></ul>
      <div class="label__car" role="img" aria-label="Photo of a gold sports car, front view"></div>
      <span class="volume">500ml</span>
    </section>

    <section class="label label--interior">
      <div class="label__sweep"></div>
      <div class="brand"><span class="brand__dot"></span><span class="brand__name">GlenV</span></div>
      <h2 class="title">Interior<br>Cleaner</h2>
      <ul class="benefits"><li>High Gloss Wax</li><li>Easy &amp; Fast</li></ul>
      <div class="label__car" role="img" aria-label="Photo of a blue sedan, front three-quarter view"></div>
      <span class="volume">500ml</span>
    </section>
  </main>
</body>
</html>
```